Criação de Papelaria Profissional para Consultoria de Negócios
" Minha missão é Ajudar as pessoas na gestão do PLANEJAMENTO E EXECUÇÃO para que identifique possibilidades de crescimento e melhoria no seu empreendimento. Ofereço: CONSULTORIA EMPRESARIAL ADMINISTRATIVA (PRESENCIAL E ONLINE) (diagnóstico, planejamento, execução e controle); CONSULTORIA ESPECIALIZADA EM GESTÃO MEI (PRESENCIAL E ONLINE) (da formalização até o monitoramento do controle) e CONSULTORIA COM TREINAMENTO (PRESENCIAL) (oficinas, cursos, dentro da empresa). "

```html
<!DOCTYPE html>
<html lang="pt-BR">
<head>
<meta charset="UTF-8">
<title>Nortevia – Papelaria</title>
<link href="https://fonts.googleapis.com/css2?family=Montserrat:wght@400;500;700&display=swap" rel="stylesheet">
<style>
  :root {
    --navy: #1b2552;
    --navy-soft: #243064;
    --blue: #3a9bd5;
    --paper: #ffffff;
    --rule: #d9dde4;
    --ink: #3a3f4b;
    --backdrop: #e9eaec;
  }
  * { margin: 0; padding: 0; box-sizing: border-box; }
  html, body { width: 1200px; height: 1200px; overflow: hidden; }
  body {
    background: var(--backdrop);
    font-family: "Montserrat", sans-serif;
    position: relative;
  }
  .sheet {
    position: absolute;
    background: var(--paper);
    box-shadow: 0 10px 28px rgba(0,0,0,.18);
    overflow: hidden;
  }
  .notepad { left: 420px; top: 48px; width: 350px; height: 504px; }
  .cover-dark { left: 288px; top: 630px; width: 300px; height: 500px; background: var(--navy); }
  .cover-light { left: 606px; top: 630px; width: 302px; height: 500px; }

  .brand { color: var(--navy); font-weight: 700; letter-spacing: .06em; line-height: 1; }
  .brand-row { display: flex; align-items: center; gap: 6px; }
  .brand-dot { width: 10px; height: 10px; background: var(--blue); }
  .tagline { font-size: 5px; font-weight: 500; letter-spacing: .08em; color: var(--ink); text-transform: uppercase; margin-top: 3px; }

  .notepad .header { position: absolute; top: 26px; left: 0; right: 0; display: flex; flex-direction: column; align-items: center; }
  .notepad .brand { font-size: 17px; }
  .notepad .header-rule { width: 120px; height: 2px; background: var(--blue); margin-top: 6px; }
  .ruled {
    position: absolute; left: 24px; right: 24px; top: 88px; height: 372px;
    background: repeating-linear-gradient(to bottom, transparent 0 11px, var(--rule) 11px 12px);
  }
  .faint-mark { position: absolute; border-radius: 18px; }
  .notepad .faint-mark { left: 95px; top: 160px; width: 160px; height: 200px; background: rgba(27,37,82,.05); }

  .contacts { position: absolute; display: flex; justify-content: space-between; align-items: center; font-size: 5px; color: var(--ink); }
  .contact { display: flex; align-items: center; gap: 3px; }
  .contact svg { width: 7px; height: 7px; flex: none; }
  .notepad .contacts { left: 24px; right: 24px; bottom: 16px; }
  .notepad .footer-band { position: absolute; left: 0; right: 0; bottom: 0; height: 5px; background: var(--navy); }
  .notepad .footer-accent { position: absolute; left: 0; bottom: 0; width: 90px; height: 5px; background: var(--blue); }

  .cover-dark .faint-mark { left: 30px; top: 50px; width: 240px; height: 340px; background: rgba(255,255,255,.06); }
  .cover-dark .footer { position: absolute; left: 18px; right: 18px; bottom: 16px; display: flex; flex-direction: column; align-items: center; gap: 8px; }
  .cover-dark .brand { color: #fff; font-size: 10px; }
  .cover-dark .tagline { color: #c9d0e4; font-size: 4px; }
  .cover-dark .contacts { position: static; width: 100%; color: #dfe4f2; font-size: 4.5px; }

  .cover-light .edge { position: absolute; left: 0; top: 0; bottom: 0; width: 22px; background: linear-gradient(to right, #eceef1, #fff); }
  .cover-light .vertical-brand {
    position: absolute; right: 18px; top: 40px;
    transform-origin: top right; transform: rotate(-90deg) translateX(-100%);
    display: flex; flex-direction: column; align-items: flex-start;
  }
  .cover-light .vertical-brand .brand { font-size: 22px; }
  .cover-light .vertical-brand .tagline { font-size: 6px; }
  .cover-light .corner-mark { position: absolute; left: 0; bottom: 0; width: 96px; height: 100px; background: var(--blue); border-top-right-radius: 22px; }
</style>
</head>
<body>

<section class="sheet notepad" aria-label="Bloco de anotações">
  <div class="header">
    <div class="brand-row"><span class="brand-dot"></span><span class="brand">NORTEVIA</span></div>
    <div class="tagline">Consultoria para Microempreendedores</div>
    <div class="header-rule"></div>
  </div>
  <div class="faint-mark"></div>
  <div class="ruled"></div>
  <div class="contacts">
    <span class="contact"><svg viewBox="0 0 10 10"><path d="M5 1a3 3 0 0 1 3 3c0 2-3 5-3 5S2 6 2 4a3 3 0 0 1 3-3z" fill="#3a9bd5"/></svg>Av. Central, 1200 - Sala 45 · CEP 00000-000</span>
    <span class="contact"><svg viewBox="0 0 10 10"><circle cx="5" cy="5" r="4" fill="#3a9bd5"/></svg>(11) 0000-0000</span>
    <span class="contact"><svg viewBox="0 0 10 10"><rect x="1" y="2.5" width="8" height="5" fill="#3a9bd5"/></svg>contato@nortevia.com</span>
  </div>
  <div class="footer-band"></div>
  <div class="footer-accent"></div>
</section>

<section class="sheet cover-dark" aria-label="Capa escura do bloco">
  <div class="faint-mark"></div>
  <div class="footer">
    <div style="display:flex;flex-direction:column;align-items:center">
      <div class="brand-row"><span class="brand-dot" style="width:7px;height:7px"></span><span class="brand">NORTEVIA</span></div>
      <div class="tagline">Consultoria para Microempreendedores</div>
    </div>
    <div class="contacts">
      <span class="contact"><svg viewBox="0 0 10 10"><path d="M5 1a3 3 0 0 1 3 3c0 2-3 5-3 5S2 6 2 4a3 3 0 0 1 3-3z" fill="#3a9bd5"/></svg>Av. Central, 1200 · Centro</span>
      <span class="contact"><svg viewBox="0 0 10 10"><circle cx="5" cy="5" r="4" fill="#3a9bd5"/></svg>(11) 0000-0000</span>
      <span class="contact"><svg viewBox="0 0 10 10"><rect x="1" y="2.5" width="8" height="5" fill="#3a9bd5"/></svg>contato@nortevia.com</span>
    </div>
  </div>
</section>

<section class="sheet cover-light" aria-label="Capa clara do bloco">
  <div class="edge"></div>
  <div class="vertical-brand">
    <div class="brand-row"><span class="brand-dot" style="width:16px;height:16px"></span><span class="brand">NORTEVIA</span></div>
    <div class="tagline">Consultoria para Microempreendedores</div>
  </div>
  <div class="corner-mark"></div>
</section>

</body>
</html>
```